Invesment management business need a stationery design

We need a stationery design for a new company based in Sao Paulo, Brazil, called "Tressily Capital". We provide investment management services for individuals and corporations.
The final design should communicate financial safety and some kind of luxury, just like an investment bank does.
As an inspiration, the designer could take a look at companies like KT Halbrook, Whitcombe Fairley, NKV or Banque Orvelle

Target Market(s)

Individuals and corporations

Industry/Entity Type

Business

Requirements
Must have
• My project must have our logo on it.
• Our business cards should have our contact information, such as telephone number and emails.

```html
<!DOCTYPE html>
<html lang="en">
<head>
<meta charset="utf-8">
<title>Tressily Capital — Stationery</title>
<link rel="stylesheet" href="https://fonts.googleapis.com/css2?family=Open+Sans:wght@300;400;600&family=Mrs+Saint+Delafield&display=swap">
<style>
  :root {
    --backdrop: #d9d9db;
    --paper: #f5f5f5;
    --ink: #2a2a2c;
    --ink-soft: #8a8a8e;
    --board: #242223;
    --board-edge: #1a1819;
    --on-board: #d6d6d8;
    --on-board-soft: #8d8b8c;
    --accent: #3a86c0;
  }
  * { box-sizing: border-box; margin: 0; padding: 0; }
  html, body { width: 1200px; height: 1000px; overflow: hidden; }
  body {
    background: var(--backdrop);
    font-family: "Open Sans", Arial, sans-serif;
    color: var(--ink);
    position: relative;
  }
  .piece { position: absolute; box-shadow: 0 6px 14px rgba(0,0,0,.18); }

  /* brand lockup */
  .brand { display: flex; align-items: center; gap: 6px; }
  .brand-dot { width: 10px; height: 10px; border-radius: 50%; background: var(--accent); flex: none; }
  .brand-name {
    font-weight: 400; text-transform: uppercase; letter-spacing: .18em;
    font-size: 8px; white-space: nowrap; color: var(--ink);
  }
  .on-dark .brand-name { color: var(--on-board); }
  .brand.large .brand-dot { width: 22px; height: 22px; }
  .brand.large { gap: 10px; }
  .brand.large .brand-name { font-size: 16px; }

  /* letterhead */
  .letterhead {
    left: 60px; top: 40px; width: 270px; height: 382px;
    background: var(--paper); padding: 26px 24px;
    font-size: 5.4px; line-height: 1.65; color: #555;
  }
  .letterhead-head { display: flex; justify-content: space-between; align-items: flex-start; margin-bottom: 34px; }
  .letterhead-contact { font-size: 4.6px; line-height: 1.6; text-align: left; color: var(--ink-soft); }
  .letterhead-contact b { color: var(--accent); font-weight: 600; }
  .letter-salutation { margin-bottom: 8px; color: var(--ink); }
  .letter-body p { margin-bottom: 9px; }
  .letter-closing { text-align: right; margin-top: 4px; font-style: italic; }
  .letter-signature {
    font-family: "Mrs Saint Delafield", cursive; font-size: 18px; color: #333;
    margin: 22px 0 0 100px; line-height: 1;
  }

  /* business cards */
  .card { width: 200px; height: 114px; background: var(--board); }
  .card-front { left: 380px; top: 120px; display: flex; align-items: center; justify-content: center; }
  .card-back { left: 610px; top: 120px; padding: 16px 16px; color: var(--on-board-soft); font-size: 5.6px; line-height: 1.7; }
  .card-back .brand { margin-bottom: 18px; }
  .card-person { color: var(--on-board); font-size: 7px; font-weight: 600; }
  .card-role { margin-bottom: 6px; }
  .card-details b { color: var(--accent); font-weight: 600; }

  /* envelopes */
  .envelope { left: 880px; width: 280px; height: 140px; background: var(--board); }
  .envelope-front { top: 40px; padding: 18px 18px; }
  .envelope-front .envelope-row { display: flex; justify-content: space-between; }
  .envelope-contact { font-size: 4.8px; line-height: 1.7; color: var(--on-board-soft); text-align: left; }
  .envelope-back { top: 210px; }
  .envelope-back svg { position: absolute; inset: 0; }
  .envelope-back .brand { position: absolute; left: 50%; top: 44px; transform: translateX(-50%); }

  /* folders */
  .folder-closed {
    left: 60px; top: 450px; width: 270px; height: 382px; background: var(--board);
    padding: 70px 0 0 50px;
  }
  .folder-open { left: 360px; top: 450px; width: 520px; height: 382px; }
  .folder-open svg { position: absolute; inset: 0; }
  .folder-open .brand { position: absolute; right: 22px; top: 268px; }
</style>
</head>
<body>

  <!-- Letterhead -->
  <article class="piece letterhead">
    <header class="letterhead-head">
      <div class="brand"><span class="brand-dot"></span><span class="brand-name">Tressily Capital</span></div>
      <address class="letterhead-contact">
        <b>A</b> Av. Paulista 1800, São Paulo<br>
        <b>T</b> Tel +55 11 4002 8921<br>
        <b>E</b> info@tressilycapital.com
      </address>
    </header>
    <p class="letter-salutation">Dear Client,</p>
    <div class="letter-body">
      <p>Thank you for placing your trust in our team. We manage every portfolio with discipline, care and a long view, seeking steady growth while protecting the capital you have built over many years.</p>
      <p>Enclosed you will find your quarterly review, with a summary of allocations, returns and the outlook prepared by our investment committee.</p>
      <p>Our advisors remain available to discuss any question about your accounts or future plans.</p>
    </div>
    <p class="letter-closing">Best regards,</p>
    <p class="letter-signature">Daniel Ferraz</p>
  </article>

  <!-- Business card, front -->
  <section class="piece card card-front on-dark">
    <div class="brand"><span class="brand-dot"></span><span class="brand-name">Tressily Capital</span></div>
  </section>

  <!-- Business card, back -->
  <section class="piece card card-back on-dark">
    <div class="brand"><span class="brand-dot"></span><span class="brand-name">Tressily Capital</span></div>
    <p class="card-person">Daniel Ferraz</p>
    <p class="card-role">Managing Partner</p>
    <p class="card-details">
      <b>T</b> +55 11 4002 8921<br>
      <b>E</b> d.ferraz@tressilycapital.com<br>
      <b>A</b> Av. Paulista 1800, São Paulo
    </p>
  </section>

  <!-- Envelope, front -->
  <section class="piece envelope envelope-front on-dark">
    <div class="envelope-row">
      <div class="brand"><span class="brand-dot"></span><span class="brand-name">Tressily Capital</span></div>
      <address class="envelope-contact">
        Av. Paulista 1800, São Paulo<br>
        +55 11 4002 8921<br>
        info@tressilycapital.com
      </address>
    </div>
  </section>

  <!-- Envelope, back with flap -->
  <section class="piece envelope envelope-back on-dark">
    <svg width="280" height="140" viewBox="0 0 280 140" aria-hidden="true">
      <path d="M0 0 L120 78 Q140 90 160 78 L280 0" fill="none" stroke="var(--board-edge)" stroke-width="1.4"/>
      <path d="M0 140 L112 72 M280 140 L168 72" fill="none" stroke="var(--board-edge)" stroke-width="1"/>
    </svg>
    <div class="brand"><span class="brand-dot"></span><span class="brand-name">Tressily Capital</span></div>
  </section>

  <!-- Presentation folder, closed -->
  <section class="piece folder-closed on-dark">
    <div class="brand large"><span class="brand-dot"></span><span class="brand-name">Tressily Capital</span></div>
  </section>

  <!-- Presentation folder, open -->
  <section class="piece folder-open on-dark">
    <svg width="520" height="382" viewBox="0 0 520 382" aria-hidden="true">
      <rect width="520" height="382" fill="var(--paper)"/>
      <line x1="260" y1="0" x2="260" y2="382" stroke="#d0d0d2" stroke-width="1"/>
      <path d="M0 252 L204 252 Q222 252 228 268 L250 382 L0 382 Z" fill="var(--board)"/>
      <path d="M296 252 L520 252 L520 382 L272 382 L280 268 Q284 252 296 252 Z" fill="var(--board)"/>
    </svg>
    <div class="brand"><span class="brand-dot"></span><span class="brand-name">Tressily Capital</span></div>
  </section>

</body>
</html>
```